Lena Corvell Business Card

I need a business card that reflects my current website: itslenacorvell.example and screenshot attached. If we keep the color scheme of the site and sample card below that would be ideal. The business card should include the information on the attached sample cards.

Industry/Entity Type

Business

```html
<!DOCTYPE html>
<html lang="en">
<head>
<meta charset="utf-8">
<title>Lena Corvell — Business Card</title>
<link rel="stylesheet" href="https://fonts.googleapis.com/css2?family=Archivo+Narrow:wght@600;700&display=swap">
<style>
  :root {
    --teal-edge: #1fa388;
    --teal-mid: #44b69d;
    --white: #ffffff;
    --panel: #e0ede9;
    --panel-shadow: #a7b3b0;
    --ink: #0d0d0d;
    --script-tone: #1c4a41;
  }
  * { margin: 0; padding: 0; box-sizing: border-box; }
  html, body {
    width: 1200px;
    height: 702px;
    overflow: hidden;
  }
  body {
    font-family: "Archivo Narrow", "Arial Narrow", sans-serif;
    background: var(--teal-edge);
  }
  .card {
    position: relative;
    width: 1200px;
    height: 702px;
    background: linear-gradient(90deg, var(--teal-edge) 0%, var(--teal-mid) 45%, var(--teal-edge) 100%);
    overflow: hidden;
  }
  .card__name {
    position: absolute;
    left: 58px;
    top: 66px;
    font-size: 42px;
    font-weight: 700;
    color: var(--white);
    letter-spacing: 0.3px;
    text-transform: uppercase;
    line-height: 1;
  }
  .card__roles {
    position: absolute;
    left: 59px;
    top: 124px;
    font-size: 24px;
    font-weight: 700;
    color: var(--white);
    line-height: 1;
  }
  .contact-panel {
    position: absolute;
    left: 59px;
    top: 174px;
    width: 574px;
    height: 246px;
    border-radius: 9px;
    background: var(--panel-shadow);
  }
  .contact-panel__face {
    position: absolute;
    inset: 0 0 14px 0;
    border-radius: 9px;
    background: var(--panel);
  }
  .contact-list {
    list-style: none;
    position: absolute;
    left: 32px;
    top: 14px;
  }
  .contact-list__item {
    display: flex;
    align-items: center;
    height: 51px;
    font-size: 25px;
    font-weight: 700;
    color: var(--ink);
  }
  .contact-list__icon {
    width: 26px;
    height: 26px;
    margin-right: 18px;
    flex-shrink: 0;
  }
  .contact-list__dot {
    width: 20px;
    height: 20px;
    border-radius: 50%;
    background: var(--ink);
    margin: 0 24px 0 2px;
    flex-shrink: 0;
  }
  .signature-mark {
    position: absolute;
    left: 597px;
    top: 462px;
    width: 542px;
    height: 180px;
    border-radius: 12px;
    background: linear-gradient(90deg, rgba(28,74,65,0.18), rgba(28,74,65,0.32));
  }
</style>
</head>
<body>
  <main class="card">
    <h1 class="card__name">Lena Corvell</h1>
    <p class="card__roles">Brand Curator I Digital Storyteller I Social Entrprenuer</p>

    <section class="contact-panel">
      <div class="contact-panel__face">
        <ul class="contact-list">
          <li class="contact-list__item">
            <svg class="contact-list__icon" viewBox="0 0 26 26" aria-hidden="true">
              <rect x="1.5" y="5.5" width="23" height="15" fill="none" stroke="#0d0d0d" stroke-width="1.6"/>
              <path d="M1.5 5.5 L13 14.5 L24.5 5.5 M1.5 20.5 L10 12.5 M24.5 20.5 L16 12.5" fill="none" stroke="#0d0d0d" stroke-width="1.4"/>
            </svg>
            me@lenacorvell.example
          </li>
          <li class="contact-list__item">
            <svg class="contact-list__icon" viewBox="0 0 26 26" aria-hidden="true">
              <path d="M20 3 C14 4 6 12 4 21 L8 24 C9 17 14 10 21 8 Z" fill="#0d0d0d"/>
              <rect x="17.5" y="2" width="6" height="6" rx="1.5" fill="#0d0d0d"/>
              <rect x="2" y="19" width="6" height="6" rx="1.5" fill="#0d0d0d"/>
            </svg>
            240.555.0142
          </li>
          <li class="contact-list__item">
            <span class="contact-list__dot" aria-hidden="true"></span>
            @itslenacorvell
          </li>
          <li class="contact-list__item">
            <svg class="contact-list__icon" viewBox="0 0 26 26" aria-hidden="true">
              <g fill="none" stroke="#0d0d0d" stroke-width="1.3">
                <circle cx="13" cy="13" r="10.5"/>
                <ellipse cx="13" cy="13" rx="4.5" ry="10.5"/>
                <path d="M2.5 13 H23.5 M4.5 7.5 H21.5 M4.5 18.5 H21.5 M13 2.5 V23.5"/>
              </g>
            </svg>
            www.itslenacorvell.example
          </li>
        </ul>
      </div>
    </section>

    <div class="signature-mark" role="img" aria-label="Hand-lettered brush script reading 'its Lena Corvell' in black ink"></div>
  </main>
</body>
</html>
```